Islamic App which helps to calculate, track and pay Zakat

We need an application which helps muslim people to calculate and pay Zakat - mandatory donations which muslim should pay based on his income. The application will consist of two parts (applications) - the one which is used by "payer" and another one - used by "receiver". To make a payment "payer" will scan QR-code which "receiver" will generate in his app and show to payer. "Receiver" will have option to initiate cash withdrawal once he collected required minimum for the withdrawal.
Important that "payer" side journey to make a payment should be as short as possible - imaging same as you make donation by cash - you just gave money and left, similar experience should be with app - couple-three taps to make it. For receiver side major requirement is to keep the UI/UX as simple as possible, these guys usually are not aware about online payments (roughly speaking this part of the app should be more similar to Lumbrela rather than to banking/financial app)
In this Figma I tried to sketch the UX for both sides (just to explain the idea): https://www.draftlynx.net/file/pkr4T8WmZtLsQbXeNcJV2a/Sketch-starter?type=design&node-id=2831-475190&mode=design

Target Market(s)

Muslims

Industry/Entity Type

Donations

Colors
0094D4
00A9DD
6FCCEA
C7EBF8
E9F6FB
00AB8E
00BBA5
67D7C9
C6EFE9
E9F9F6

Requirements
Must have
• The application should have soul. Design should show that this application intend to help people, not just money transfer
Nice to have
• Payment should be as quick as possible, in the sketches I showed it as banknotes/coins which user need to slide-up to pay. Maybe make it similar as Vexa RT dock icons?
Should not have
• The application should not look as banking/financial app or wallet app

```html
<!DOCTYPE html>
<html lang="en">
<head>
<meta charset="utf-8">
<title>Sadaqo – Zakat App Screens</title>
<link href="https://fonts.googleapis.com/css2?family=Inter:wght@300;400;500;600;700;800&display=swap" rel="stylesheet">
<style>
:root{
  --canvas:#8fb3d8;
  --sky:#0094d4;
  --sky-mid:#00a9dd;
  --sky-soft:#6fccea;
  --sky-pale:#c7ebf8;
  --sky-mist:#e9f6fb;
  --teal:#00ab8e;
  --teal-mid:#00bba5;
  --teal-soft:#67d7c9;
  --teal-pale:#c6efe9;
  --teal-mist:#e9f9f6;
  --ink:#1f2f3a;
  --muted:#5f6f78;
  --label:#6f7f88;
  --field-line:#d6e8ef;
  --white:#ffffff;
}
*{box-sizing:border-box;margin:0;padding:0}
html,body{width:1163px;height:1200px;overflow:hidden}
body{background:var(--canvas);font-family:'Inter',sans-serif;position:relative;color:var(--ink)}
.screen{position:absolute;width:225px;height:502px;border-radius:12px;overflow:hidden;background:var(--white);box-shadow:0 14px 30px rgba(20,70,110,.22)}
.hero{position:absolute;inset:0;background:linear-gradient(165deg,var(--sky) 0%,var(--sky-mid) 45%,var(--teal-mid) 100%)}
.status{position:absolute;top:8px;left:8px;right:8px;display:flex;justify-content:space-between;align-items:center;color:var(--white);font-size:9px;font-weight:600}
.status-right{display:flex;align-items:center;gap:3px;font-size:7px}
.back{position:absolute;left:14px;top:33px;width:18px;height:18px;border:1px solid rgba(255,255,255,.7);border-radius:50%;display:flex;align-items:center;justify-content:center}
.title{position:absolute;left:14px;color:var(--white);font-size:14.5px;font-weight:600;line-height:18px}
.subtitle{position:absolute;left:14px;color:var(--sky-mist);font-size:6.5px}
.sheet{position:absolute;left:0;right:0;bottom:0;background:var(--white);border-radius:21px 21px 0 0}
.sheet.soft{background:var(--sky-mist)}
.toggle{position:absolute;left:14px;width:197px;height:31px;border-radius:16px;background:var(--sky-pale);display:flex;padding:3px;font-size:8px}
.toggle span{flex:1;display:flex;align-items:center;justify-content:center;color:var(--muted);border-radius:14px}
.toggle span.on{background:var(--white);color:var(--ink);font-weight:500;box-shadow:0 1px 3px rgba(0,0,0,.08)}
.field{position:absolute;left:14px;width:197px;height:31px;border:1px solid var(--field-line);border-radius:16px;display:flex;align-items:center;padding-left:14px;gap:7px;font-size:8px;color:#44545d}
.btn{position:absolute;left:14px;width:197px;height:33px;border-radius:17px;background:var(--teal);color:var(--white);font-size:9.5px;font-weight:600;display:flex;align-items:center;justify-content:center}
.row-note{position:absolute;left:14px;width:197px;display:flex;justify-content:space-between;font-size:6.5px;color:#44545d}
.row-note .link{color:var(--sky);font-weight:600}
.check{display:inline-block;width:8px;height:8px;border:1px solid #9aa8ae;border-radius:2px;vertical-align:-1px;margin-right:4px}
.divider{position:absolute;left:32px;width:161px;display:flex;align-items:center;gap:5px;font-size:6.5px;color:#44545d;font-weight:500}
.divider::before,.divider::after{content:"";flex:1;height:1px;background:var(--field-line)}
.social{position:absolute;width:96px;height:32px;border:1px solid var(--field-line);border-radius:16px;display:flex;align-items:center;justify-content:center;gap:5px;font-size:8px;color:#44545d}
.social i{width:7px;height:7px;border-radius:50%;background:var(--sky);display:block}
.splash{background:linear-gradient(180deg,var(--white) 0%,var(--teal-mist) 100%)}
.wordmark{position:absolute;left:0;top:195px;width:225px;text-align:center;font-size:29px;font-weight:800;letter-spacing:-.5px;line-height:32px;color:var(--teal)}
.start{position:absolute;left:50px;top:400px;width:129px;height:30px;border-radius:15px;background:var(--teal);color:var(--white);font-size:13px;font-weight:400;display:flex;align-items:center;justify-content:center}
.caption{position:absolute;top:601px;width:225px;text-align:center;color:var(--white);font-size:13.5px;font-weight:500}
.avatar{position:absolute;border-radius:50%;background:radial-gradient(circle at 50% 40%,#8a6a55,#3d3a36 70%);border:2px solid rgba(255,255,255,.5)}
.avatar.dark{background:radial-gradient(circle at 50% 40%,#5a3a30,#1e1a1a 70%)}
.edit-badge{position:absolute;width:13px;height:13px;background:var(--teal);border:1.5px solid var(--white);border-radius:3px;display:flex;align-items:center;justify-content:center}
.welcome{position:absolute;left:94px;color:var(--white);font-size:10px;font-weight:300}
.name{position:absolute;left:94px;color:var(--white);font-size:14.5px;font-weight:700}
.balance{position:absolute;left:94px;top:80px;color:var(--white);font-size:7px;display:flex;align-items:baseline;gap:4px}
.balance b{font-size:14.5px;font-weight:700}
.balance small{font-size:7px;font-weight:700;margin-left:-3px}
.tile{position:absolute;width:72px;height:71px;background:var(--white);border-radius:8px;box-shadow:0 2px 6px rgba(0,80,110,.06);display:flex;align-items:center;justify-content:center}
.tile-label{position:absolute;width:90px;text-align:center;font-size:9.5px;line-height:11px;color:var(--label)}
.flag{display:block;width:18px;height:11px;position:relative;background:linear-gradient(180deg,#0a9a4a 0 33%,#fff 33% 66%,#111 66%)}
.flag::before{content:"";position:absolute;left:0;top:0;width:5px;height:11px;background:#e0242b}
.textarea{height:85px;align-items:flex-start;padding-top:12px;border-radius:18px}
.skip{position:absolute;right:12px;top:36px;color:var(--sky-mist);font-size:6.5px}
.rule{position:absolute;left:94px;top:72px;width:90px;height:1px;background:rgba(255,255,255,.55)}
.ic-a{fill:var(--sky)}
.ic-b{fill:var(--teal-soft)}
.ic-w{fill:var(--white)}
.st-a{stroke:var(--teal);fill:none;stroke-width:.9}
.st-w{stroke:var(--white);fill:none}
</style>
</head>
<body>

<section class="screen splash">
  <div class="wordmark">Sadaqo</div>
  <div class="start">Get Started</div>
</section>

<section class="screen" style="left:336px;top:66px">
  <div class="hero"></div>
  <div class="status"><span>08:34</span><span class="status-right"><svg width="10" height="7"><rect x="0" y="5" width="2" height="2" class="ic-w"/><rect x="3" y="3" width="2" height="4" class="ic-w"/><rect x="6" y="1" width="2" height="6" class="ic-w"/></svg>4G<svg width="15" height="7"><rect x=".5" y=".5" width="12" height="6" rx="1.5" class="st-w"/><rect x="2" y="2" width="6" height="3" fill="#f2c230"/><rect x="13" y="2" width="1.5" height="3" class="ic-w"/></svg></span></div>
  <div class="back"><svg width="8" height="8" viewBox="0 0 8 8"><path d="M7 4H1M3.5 1.5 1 4l2.5 2.5" class="st-w"/></svg></div>
  <div class="title" style="top:77px">Create your account</div>
  <div class="subtitle" style="top:102px">Sign in-up to enjoy the best managing experience</div>
  <div class="sheet" style="top:126px"></div>
  <div class="toggle" style="top:141px"><span>Payer</span><span class="on">Reciever</span></div>
  <div class="field" style="top:186px"><svg width="10" height="10" viewBox="0 0 10 10"><circle cx="5" cy="3" r="2.2" class="st-a"/><path d="M1 9.5c0-2.5 2-3.5 4-3.5s4 1 4 3.5z" class="st-a"/></svg>Full Name</div>
  <div class="field" style="top:225px"><svg width="11" height="9" viewBox="0 0 11 9"><rect x=".5" y=".5" width="10" height="8" rx="1" class="st-a"/><path d="M.5 1 5.5 5l5-4" class="st-a"/></svg>Email-ID</div>
  <div class="field" style="top:265px"><svg width="9" height="11" viewBox="0 0 9 11"><rect x=".5" y="4.5" width="8" height="6" rx="1" class="st-a"/><path d="M2.5 4.5V3a2 2 0 0 1 4 0v1.5" class="st-a"/></svg>Password</div>
  <div class="field" style="top:305px"><svg width="10" height="10" viewBox="0 0 10 10"><path d="M2 .8 3.8 3 2.8 4.2a6 6 0 0 0 3 3L7 6.2l2.2 1.8L8 9.4C4.5 9.4.6 5.5.6 2z" class="st-a"/></svg>Phone No.</div>
  <div class="btn" style="top:350px">Register</div>
</section>

<section class="screen" style="left:601px;top:66px">
  <div class="hero"></div>
  <div class="status"><span>08:34</span><span class="status-right"><svg width="10" height="7"><rect x="0" y="5" width="2" height="2" class="ic-w"/><rect x="3" y="3" width="2" height="4" class="ic-w"/><rect x="6" y="1" width="2" height="6" class="ic-w"/></svg>4G<svg width="15" height="7"><rect x=".5" y=".5" width="12" height="6" rx="1.5" class="st-w"/><rect x="2" y="2" width="6" height="3" fill="#f2c230"/><rect x="13" y="2" width="1.5" height="3" class="ic-w"/></svg></span></div>
  <div class="back"><svg width="8" height="8" viewBox="0 0 8 8"><path d="M7 4H1M3.5 1.5 1 4l2.5 2.5" class="st-w"/></svg></div>
  <div class="title" style="top:77px">Go ahead and set up<br>your account</div>
  <div class="subtitle" style="top:121px">Sign in-up to enjoy the best managing experience</div>
  <div class="sheet" style="top:148px"></div>
  <div class="toggle" style="top:164px"><span class="on">Payer</span><span>Reciever</span></div>
  <div class="field" style="top:210px"><svg width="11" height="9" viewBox="0 0 11 9"><rect x=".5" y=".5" width="10" height="8" rx="1" class="st-a"/><path d="M.5 1 5.5 5l5-4" class="st-a"/></svg>E-mail ID</div>
  <div class="field" style="top:250px"><svg width="9" height="11" viewBox="0 0 9 11"><rect x=".5" y="4.5" width="8" height="6" rx="1" class="st-a"/><path d="M2.5 4.5V3a2 2 0 0 1 4 0v1.5" class="st-a"/></svg>Password</div>
  <div class="row-note" style="top:291px"><span><i class="check"></i>Remember me</span><span class="link">Forget Password?</span></div>
  <div class="btn" style="top:315px">Login</div>
  <div class="divider" style="top:366px">Or login with</div>
  <div class="social" style="left:14px;top:394px"><i></i>Glimmo</div>
  <div class="social" style="left:115px;top:394px"><i></i>Orchard</div>
</section>

<section class="screen" style="left:867px;top:66px">
  <div class="hero"></div>
  <div class="status"><span>08:34</span><span class="status-right"><svg width="10" height="7"><rect x="0" y="5" width="2" height="2" class="ic-w"/><rect x="3" y="3" width="2" height="4" class="ic-w"/><rect x="6" y="1" width="2" height="6" class="ic-w"/></svg>4G<svg width="15" height="7"><rect x=".5" y=".5" width="12" height="6" rx="1.5" class="st-w"/><rect x="2" y="2" width="6" height="3" fill="#f2c230"/><rect x="13" y="2" width="1.5" height="3" class="ic-w"/></svg></span></div>
  <div class="back"><svg width="8" height="8" viewBox="0 0 8 8"><path d="M7 4H1M3.5 1.5 1 4l2.5 2.5" class="st-w"/></svg></div>
  <div class="title" style="top:77px">Forgot your<br>password?</div>
  <div class="subtitle" style="top:121px">Enter your email address to reset your password</div>
  <div class="sheet" style="top:148px"></div>
  <div class="field" style="top:164px"><svg width="11" height="9" viewBox="0 0 11 9"><rect x=".5" y=".5" width="10" height="8" rx="1" class="st-a"/><path d="M.5 1 5.5 5l5-4" class="st-a"/></svg>Your E-mail</div>
  <div class="btn" style="top:208px">Reset</div>
</section>

<div class="caption" style="left:203px">Profile Screen</div>
<div class="caption" style="left:469px">Payer Dashboard</div>
<div class="caption" style="left:734px">Reciever Dashboard</div>

<section class="screen" style="left:203px;top:633px">
  <div class="hero"></div>
  <div class="status"><span>08:34</span><span class="status-right"><svg width="10" height="7"><rect x="0" y="5" width="2" height="2" class="ic-w"/><rect x="3" y="3" width="2" height="4" class="ic-w"/><rect x="6" y="1" width="2" height="6" class="ic-w"/></svg>4G<svg width="15" height="7"><rect x=".5" y=".5" width="12" height="6" rx="1.5" class="st-w"/><rect x="2" y="2" width="6" height="3" fill="#f2c230"/><rect x="13" y="2" width="1.5" height="3" class="ic-w"/></svg></span></div>
  <div class="back"><svg width="8" height="8" viewBox="0 0 8 8"><path d="M7 4H1M3.5 1.5 1 4l2.5 2.5" class="st-w"/></svg></div>
  <div class="skip">Skip for now</div>
  <div class="title" style="top:76px">Setup your Profile</div>
  <div class="subtitle" style="top:102px">Setup your profile to enjoy the best managing experience</div>
  <div class="sheet" style="top:125px"></div>
  <div class="avatar" role="img" aria-label="Profile photo of the user" style="left:82px;top:139px;width:62px;height:62px"></div>
  <div class="edit-badge" style="left:128px;top:183px"><svg width="7" height="7" viewBox="0 0 7 7"><path d="M1 6 1.3 4.6 4.8 1.1 5.9 2.2 2.4 5.7z" class="ic-w"/></svg></div>
  <div class="field" style="top:215px">What’s your name?</div>
  <div class="field" style="top:252px">Select your Gender</div>
  <div class="field" style="top:289px;gap:14px"><span class="flag" role="img" aria-label="UAE flag"></span>Phone number</div>
  <div class="field textarea" style="top:329px">Your Description here...</div>
  <div class="btn" style="top:438px">Save</div>
</section>

<section class="screen" style="left:469px;top:633px">
  <div class="hero"></div>
  <div class="status"><span>08:34</span><span class="status-right"><svg width="10" height="7"><rect x="0" y="5" width="2" height="2" class="ic-w"/><rect x="3" y="3" width="2" height="4" class="ic-w"/><rect x="6" y="1" width="2" height="6" class="ic-w"/></svg>4G<svg width="15" height="7"><rect x=".5" y=".5" width="12" height="6" rx="1.5" class="st-w"/><rect x="2" y="2" width="6" height="3" fill="#f2c230"/><rect x="13" y="2" width="1.5" height="3" class="ic-w"/></svg></span></div>
  <div class="avatar" role="img" aria-label="Payer profile photo" style="left:20px;top:32px;width:62px;height:62px"></div>
  <div class="welcome" style="top:49px">Welcome</div>
  <div class="name" style="top:60px">Idris Karam</div>
  <div class="sheet soft" style="top:110px"></div>

  <div class="tile" style="left:28px;top:137px"><svg width="30" height="30" viewBox="0 0 30 30"><path d="M2 14 28 3 20 28 14 17z" class="ic-a"/><path d="M14 17 28 3 17 27z" class="ic-b"/></svg></div>
  <div class="tile-label" style="left:19px;top:215px">Send<br>Money</div>
  <div class="tile" style="left:124px;top:137px"><svg width="32" height="32" viewBox="0 0 32 32"><rect x="0" y="0" width="15" height="15" rx="2" class="ic-a"/><rect x="17" y="0" width="15" height="15" rx="2" class="ic-b"/><rect x="0" y="17" width="15" height="15" rx="2" class="ic-b"/><rect x="17" y="17" width="15" height="15" rx="2" class="ic-a"/><path d="M7.5 4v7M4 7.5h7M21 7.5h7M4.5 21.5l6 6M10.5 21.5l-6 6M21 22h7M21 26h7" class="st-w" stroke-width="2"/></svg></div>
  <div class="tile-label" style="left:115px;top:215px">Calculate<br>Zaqat</div>
  <div class="tile" style="left:28px;top:248px"><svg width="32" height="32" viewBox="0 0 32 32"><path d="M8 2h14l6 6v22H8z" class="ic-a"/><path d="M13 12h10M13 17h10M13 22h10" class="st-w" stroke-width="2"/><circle cx="8" cy="24" r="7" class="ic-b" stroke="#fff" stroke-width="1.5"/><path d="M8 20v4h3" class="st-w" stroke-width="1.5"/></svg></div>
  <div class="tile-label" style="left:19px;top:326px">Transaction<br>History</div>
  <div class="tile" style="left:124px;top:248px"><svg width="34" height="30" viewBox="0 0 34 30"><path d="M8 10 22 1l6 9z" class="ic-b"/><rect x="1" y="9" width="32" height="20" rx="2" class="ic-a"/><path d="M6 16h6M6 23h4M13 23h4M20 23h4M27 23h3" class="st-w" stroke-width="2"/></svg></div>
  <div class="tile-label" style="left:115px;top:326px">Add Payment<br>Details</div>
  <div class="tile" style="left:28px;top:359px"><svg width="34" height="30" viewBox="0 0 34 30"><circle cx="9" cy="6" r="5" class="ic-b"/><path d="M0 24c0-7 4-10 9-10s9 3 9 10z" class="ic-b"/><path d="M14 26 16 20 29 7l4 4-13 13z" class="ic-a"/></svg></div>
  <div class="tile-label" style="left:19px;top:437px">Edit<br>Profile</div>
  <div class="tile" style="left:124px;top:359px"><svg width="32" height="32" viewBox="0 0 32 32"><path d="M13 1h6l1 4 4 2 4-2 4 4-2 4 2 4 4 1v6l-4 1-2 4 2 4-4 4-4-2-4 2-1 4h-6l-1-4-4-2-4 2-4-4 2-4-2-4-4-1v-6l4-1 2-4-2-4 4-4 4 2 4-2z" transform="scale(.84) translate(2 2)" class="ic-a"/><circle cx="16" cy="16" r="5" class="ic-w"/></svg></div>
  <div class="tile-label" style="left:115px;top:437px">Settings</div>
</section>

<section class="screen" style="left:734px;top:633px">
  <div class="hero"></div>
  <div class="status"><span>08:34</span><span class="status-right"><svg width="10" height="7"><rect x="0" y="5" width="2" height="2" class="ic-w"/><rect x="3" y="3" width="2" height="4" class="ic-w"/><rect x="6" y="1" width="2" height="6" class="ic-w"/></svg>4G<svg width="15" height="7"><rect x=".5" y=".5" width="12" height="6" rx="1.5" class="st-w"/><rect x="2" y="2" width="6" height="3" fill="#f2c230"/><rect x="13" y="2" width="1.5" height="3" class="ic-w"/></svg></span></div>
  <div class="avatar dark" role="img" aria-label="Receiver profile photo" style="left:20px;top:32px;width:62px;height:62px"></div>
  <div class="welcome" style="top:37px">Welcome</div>
  <div class="name" style="top:48px">Yusuf Noor</div>
  <div class="rule"></div>
  <div class="balance">Your Balance: <b>600</b><small>AED</small></div>
  <div class="sheet soft" style="top:110px"></div>

  <div class="tile" style="left:28px;top:137px"><svg width="34" height="30" viewBox="0 0 34 30"><circle cx="19" cy="5" r="4" class="ic-b"/><circle cx="24" cy="13" r="3" class="ic-b"/><rect x="1" y="14" width="5" height="14" class="ic-a"/><path d="M8 15h8l4 3h8c3 0 4 3 2 4l-10 6H8z" class="ic-a"/></svg></div>
  <div class="tile-label" style="left:19px;top:215px">Receive<br>Money</div>
  <div class="tile" style="left:124px;top:137px"><svg width="32" height="32" viewBox="0 0 32 32"><rect x="0" y="0" width="32" height="32" class="ic-a"/><rect x="3" y="3" width="11" height="11" class="ic-w"/><rect x="5" y="5" width="7" height="7" class="ic-a"/><rect x="18" y="3" width="11" height="11" class="ic-w"/><rect x="20" y="5" width="7" height="7" class="ic-a"/><rect x="3" y="18" width="11" height="11" class="ic-w"/><rect x="5" y="20" width="7" height="7" class="ic-a"/><rect x="18" y="18" width="4" height="4" class="ic-w"/><rect x="25" y="18" width="4" height="4" class="ic-w"/><rect x="18" y="25" width="4" height="4" class="ic-w"/><rect x="25" y="25" width="4" height="4" class="ic-w"/></svg></div>
  <div class="tile-label" style="left:115px;top:215px">QR Code<br>Generator</div>
  <div class="tile" style="left:28px;top:248px"><svg width="32" height="32" viewBox="0 0 32 32"><path d="M8 2h14l6 6v22H8z" class="ic-a"/><path d="M13 12h10M13 17h10M13 22h10" class="st-w" stroke-width="2"/><circle cx="8" cy="24" r="7" class="ic-b" stroke="#fff" stroke-width="1.5"/><path d="M8 20v4h3" class="st-w" stroke-width="1.5"/></svg></div>
  <div class="tile-label" style="left:19px;top:326px">Transaction<br>History</div>
  <div class="tile" style="left:124px;top:248px"><svg width="34" height="30" viewBox="0 0 34 30"><circle cx="9" cy="6" r="5" class="ic-b"/><path d="M0 24c0-7 4-10 9-10s9 3 9 10z" class="ic-b"/><path d="M14 26 16 20 29 7l4 4-13 13z" class="ic-a"/></svg></div>
  <div class="tile-label" style="left:115px;top:326px">Edit<br>Profile</div>
  <div class="tile" style="left:28px;top:359px"><svg width="32" height="32" viewBox="0 0 32 32"><path d="M13 1h6l1 4 4 2 4-2 4 4-2 4 2 4 4 1v6l-4 1-2 4 2 4-4 4-4-2-4 2-1 4h-6l-1-4-4-2-4 2-4-4 2-4-2-4-4-1v-6l4-1 2-4-2-4 4-4 4 2 4-2z" transform="scale(.84) translate(2 2)" class="ic-a"/><circle cx="16" cy="16" r="5" class="ic-w"/></svg></div>
  <div class="tile-label" style="left:19px;top:437px">Settings</div>
</section>

</body>
</html>
```